FR / EN Beekeeper research design packaging / label; Beekeeper looking for a design package

I need as a beekeeper to create a design to better showcase my honey. Indeed I work in a natural environment of high quality on a hill called "Veldmoor" (many flowers different fields, few pesticides, ...). I practice a beekeeping respectful of the bee and in a traditional way. I produce a high quality honey (luxury product) for a wealthy clientele looking for good health products, ... The main label should contain only the following text (accompanied by an image): The Veldmoor Honey A variant would also be useful for my production of mead (alcohol from the fermentation of honey): The Veldmoor mead In terms of form, given the target audience, I thought I was moving towards a modern label against a background black and with golden patterns. An example is the honey of the wonders attached, we find a honey assimilated as a real luxury product. Same in the Cuvée Lando Perrusi attachment. I would like to move towards these tones of colors by adding a touch more "champêtre" as on the label of the bottle of wine below where one sees golden flowers drawn, of light and subtle way. Another example that I like is that of the bee of ree joined. Another modern idea identified on this site is this design: https://www.artpitchhub.com/design/30418822 https: //www.artpitchhub. com / design / 30418957 I would also need a round label to place on the lid of the pot with indications of signs (my address) as well as additional information about my product: - BALDUCCI Armand - Veldmoor, 14 - 6812 Hautvelin - 500 g - Spring harvest - Honey all flowers - Flora: rapeseed, fruit trees, clovers - Flavors: sweet honey with vegetal notes Remarks: this is my first artpitchhub project, if you are surprised by some points of the brief or it is missing important information do not hesitate to let me know! ************************************************** ******************************* ENGLISH ****************** ************** I need to beekeeper a new design Indeed, I work in a very natural environment, a high quality eco-system which is the south of Belgium (many different flowers in the fields, few pesticides, ...). I practice a natural beekeeping, in an artisanal way I produce a high quality honey (luxuous product) for wealthy people who are looking for good and healthy products. The following description: The Veldmoor Honey A slight variation could be useful for my production (alcohol from honey fermentation): The Veldmoor Meads Concerning the form, a modern design with golden patterns on a black background could be appropriate. An example is the honey of the wonders in attachment, we could see that honey in this case is a branded like a very luxuous product. I wish to go for these last colors with a more "rural touch" as attachment. We can see golden flowers in a light and elegant manner. Another interesting example is the honey bee in attachment. Some example found on this site: https://www.artpitchhub.com/design/30418822 https: //www.artpitchhub. com / design / 30418957 Balducci Armand - Veldmoor, 14 - 6812 Hautvelin - 500 g - Spring Harvest - Honey all flowers - Flora: rapeseed, fruit, clovers - Flavors: sweet honey with vegetal notes

Target Market(s)

affluent clientele looking for natural products, good for health, ...

Industry/Entity Type

Agriculture

Font styles to use
Decorative
Script
Other font styles liked:
• à la libre appréciation du designer, tant que c'est moderne et élégant

Requirements
Must have
• All text must be in French / A main label and a round label on the lid of the jar. Gilding (preferably on a black background). An image accompanying the text. Gold on a black background
Nice to have
• Elegant and modern design Elegant and modern design
Should not have
• Do not load too much the main label, it must remain uncluttered

```html
<!DOCTYPE html>
<html lang="fr">
<head>
<meta charset="utf-8">
<title>The Veldmoor Honey – étiquettes</title>
<link rel="stylesheet" href="https://fonts.googleapis.com/css2?family=Cinzel:wght@500;700&family=Libre+Caslon+Text:wght@700&family=Open+Sans:wght@500;600&display=swap">
<style>
  :root {
    --backdrop-light: #d9d9d9;
    --backdrop-dark: #9a9a9a;
    --label-black: #0d0c0b;
    --gold: #d8ac3e;
    --gold-soft: #b8912f;
    --copper-dark: #5a2a0c;
    --copper: #b8652a;
    --copper-light: #f3c98e;
  }
  * { margin: 0; padding: 0; box-sizing: border-box; }
  html, body { width: 1200px; height: 1200px; overflow: hidden; }
  body {
    background: radial-gradient(ellipse at 50% 55%, var(--backdrop-light) 0%, #c4c4c4 45%, var(--backdrop-dark) 100%);
    position: relative;
  }

  /* Main jar label */
  .main-label {
    position: absolute;
    left: 130px; top: 420px;
    width: 470px; height: 370px;
    background: var(--label-black);
    overflow: hidden;
  }
  .copper-band {
    position: absolute; left: 0; right: 0; height: 14px;
    background: linear-gradient(90deg, var(--copper-dark) 0%, var(--copper) 18%, var(--copper-light) 32%, var(--copper) 48%, var(--copper-dark) 62%, var(--copper) 78%, var(--copper-light) 90%, var(--copper-dark) 100%);
  }
  .copper-band.top { top: 0; }
  .copper-band.bottom { bottom: 0; }
  .honeycomb {
    position: absolute;
    background: linear-gradient(160deg, #c9a53c, #8d7224);
  }
  .honeycomb.upper-right {
    right: 0; top: 62px; width: 64px; height: 108px;
    clip-path: polygon(30% 0, 100% 0, 100% 100%, 30% 100%, 0 75%, 0 25%);
  }
  .honeycomb.lower-left {
    left: 0; bottom: 34px; width: 70px; height: 120px;
    clip-path: polygon(0 0, 70% 0, 100% 25%, 100% 75%, 70% 100%, 0 100%);
  }
  .brand-mark {
    position: absolute; left: 0; right: 0; top: 54px;
    display: flex; align-items: center; justify-content: center; gap: 10px;
    font-family: "Cinzel", serif; font-weight: 700;
    font-size: 17px; letter-spacing: 1px; color: var(--gold);
  }
  .brand-dot {
    width: 16px; height: 16px; border-radius: 50%;
    background: var(--gold);
  }
  .product-title {
    position: absolute; left: 0; right: 0; top: 168px;
    text-align: center;
    font-family: "Cinzel", serif; font-weight: 700;
    color: var(--gold); line-height: 1.05;
  }
  .product-title .line-small { display: block; font-size: 36px; letter-spacing: 1px; }
  .product-title .rule {
    display: block; width: 250px; height: 2px; margin: 6px auto 4px;
    background: var(--gold-soft);
  }
  .net-weight {
    position: absolute; right: 12px; bottom: 30px;
    border: 1.5px solid var(--gold); border-radius: 3px;
    padding: 1px 5px;
    font-family: "Libre Caslon Text", serif; font-weight: 700;
    font-size: 17px; color: var(--gold);
  }

  /* Seal strip */
  .seal-strip {
    position: absolute;
    left: 612px; top: 300px;
    width: 40px; height: 195px;
    background: var(--label-black);
    border-left: 3px solid var(--copper);
    border-right: 3px solid var(--copper);
    display: flex; flex-direction: column; align-items: center; justify-content: space-between;
    padding: 8px 0;
  }
  .seal-strip .seal-dot {
    width: 22px; height: 22px; border-radius: 50%; background: var(--gold); flex: none;
  }
  .seal-strip .seal-text {
    writing-mode: vertical-rl;
    font-family: "Cinzel", serif; font-weight: 500;
    font-size: 9px; letter-spacing: 0; color: var(--gold);
    white-space: nowrap;
  }

  /* Lid label */
  .lid-label {
    position: absolute;
    left: 680px; top: 380px;
    width: 440px; height: 440px;
  }
  .lid-label svg { display: block; }
  .arc-text {
    font-family: "Open Sans", sans-serif; font-weight: 500;
    font-size: 16px; fill: var(--gold);
  }
  .lid-content {
    position: absolute; inset: 0;
    display: flex; flex-direction: column; align-items: center;
    padding-top: 66px;
    color: var(--gold); text-align: center;
  }
  .lid-content .brand-mark {
    position: static; font-size: 14px; gap: 8px; margin-bottom: 66px;
  }
  .lid-content .brand-dot { width: 13px; height: 13px; }
  .producer-name {
    font-family: "Libre Caslon Text", serif; font-weight: 700;
    font-size: 25px; letter-spacing: 0.3px; line-height: 32px;
  }
  .name-rule {
    position: relative;
    width: 250px; height: 2px; margin: 6px 0 10px;
    background: var(--gold);
  }
  .name-rule::before, .name-rule::after {
    content: ""; position: absolute; top: -3px;
    width: 8px; height: 8px; background: var(--gold);
    transform: rotate(45deg);
  }
  .name-rule::before { left: -4px; }
  .name-rule::after { right: -4px; }
  .info-line {
    font-family: "Open Sans", sans-serif; font-weight: 500;
    font-size: 22px; line-height: 32px;
  }
  .info-rule { width: 220px; height: 1.5px; background: var(--gold); margin: 2px 0 3px; }
</style>
</head>
<body>

<section class="main-label" aria-label="Étiquette principale">
  <div class="copper-band top"></div>
  <div class="honeycomb upper-right" role="img" aria-label="Motif d'alvéoles dorées"></div>
  <div class="honeycomb lower-left" role="img" aria-label="Motif d'alvéoles dorées"></div>
  <div class="brand-mark"><span class="brand-dot"></span><span>The Veldmoor Honey</span></div>
  <h1 class="product-title">
    <span class="line-small">THE</span>
    <span class="line-small">VELDMOOR</span>
    <span class="rule"></span>
    <span class="line-small">HONEY</span>
  </h1>
  <div class="net-weight">500g</div>
  <div class="copper-band bottom"></div>
</section>

<aside class="seal-strip" aria-label="Bande de scellé">
  <span class="seal-dot"></span>
  <span class="seal-text">THE VELDMOOR HONEY</span>
  <span class="seal-dot"></span>
</aside>

<section class="lid-label" aria-label="Étiquette de couvercle">
  <svg width="440" height="440" viewBox="0 0 440 440">
    <defs>
      <linearGradient id="copperRing" x1="0" y1="0" x2="1" y2="1">
        <stop offset="0" stop-color="#f3c98e"/>
        <stop offset="0.3" stop-color="#b8652a"/>
        <stop offset="0.55" stop-color="#5a2a0c"/>
        <stop offset="0.8" stop-color="#d58a45"/>
        <stop offset="1" stop-color="#5a2a0c"/>
      </linearGradient>
      <path id="lidArc" d="M220,32 A188,188 0 1 0 220,408 A188,188 0 1 0 220,32"/>
    </defs>
    <circle cx="220" cy="220" r="219" fill="#0d0c0b"/>
    <circle cx="220" cy="220" r="208" fill="none" stroke="url(#copperRing)" stroke-width="5"/>
    <text class="arc-text"><textPath href="#lidArc" startOffset="30%" text-anchor="middle">Flora: rapeseed, fruit trees, clovers</textPath></text>
    <text class="arc-text"><textPath href="#lidArc" startOffset="49%" text-anchor="middle">500 g</textPath></text>
    <text class="arc-text"><textPath href="#lidArc" startOffset="70%" text-anchor="middle">Flavors: sweet honey with vegetal notes</textPath></text>
  </svg>
  <div class="lid-content">
    <div class="brand-mark"><span class="brand-dot"></span><span>The Veldmoor Honey</span></div>
    <div class="producer-name">BALDUCCI Armand</div>
    <div class="name-rule"></div>
    <div class="info-line">Veldmoor, 14</div>
    <div class="info-line">6812 Hautvelin</div>
    <div class="info-rule"></div>
    <div class="info-line">Harvest spring</div>
    <div class="info-line">Honey all flowers</div>
  </div>
</section>

</body>
</html>
```